Catalog Design for herbal supplement products

We need a product catalog for several of our new dietary supplement products. We specialize in herbal formula, so we want our catalog to have some pictures of herbs, greens, flowers, plants for nature's feeling. We would like to see the catalog matches the color of our logo ( attached file). We need a text area with clear, readable fond and size for product description.

P.S.: I just upload another file called "catalog sample", please go and checkout this picture and see what kind of feeling I'm looking for. Please DO NOT just copy the catalog design from this sample. I'm just giving you a feeling of the catalog I want.

Product

Sans Serif

Requirements
Must have
• one page must display 2~3 products, with bottles pics, supplement fact table, text area for description.
• professional looking, neat and clean displays
• easy to read fond, size text
• good layout between bottles pics, supplement fact tables, texts and herbal images
Nice to have
• high quality, copyright-free herbs, greens, flowers, plants images associated with co-related products to decorate the catalog
Should not have
• must NOT be overly messy and hard-to-read

```html
<!DOCTYPE html>
<html lang="en">
<head>
<meta charset="utf-8">
<title>Verdalia Supplement Catalog</title>
<link href="https://fonts.googleapis.com/css2?family=Montserrat:wght@400;500;700&display=swap" rel="stylesheet">
<style>
  :root {
    --leaf: #8cc63f;
    --leaf-light: #c8e68a;
    --leaf-pale: #eef7dc;
    --leaf-dark: #5d9c2a;
    --bark: #5a2e14;
    --bark-light: #8a4a22;
    --bottle-dark: #123d22;
    --bottle: #1f5a34;
    --bottle-shine: #2f7a48;
    --ink: #2d2d2d;
    --paper: #ffffff;
    --stage: #2b2b2b;
  }
  * { box-sizing: border-box; margin: 0; padding: 0; }
  html, body { width: 1200px; height: 1200px; overflow: hidden; }
  body {
    background: var(--stage);
    font-family: "Montserrat", sans-serif;
    color: var(--ink);
    position: relative;
  }
  .spread {
    position: absolute;
    left: 210px;
    width: 780px;
    height: 560px;
    display: flex;
  }
  .spread--outer { top: 30px; }
  .spread--inner { top: 610px; }
  .page {
    position: relative;
    width: 390px;
    height: 560px;
    background: var(--paper);
    overflow: hidden;
  }
  .page--tinted {
    background: linear-gradient(200deg, var(--leaf-light) 0%, var(--leaf-pale) 45%, #fff 80%);
  }
  .page-art { position: absolute; inset: 0; width: 100%; height: 100%; }
  .product-list {
    position: absolute;
    left: 26px;
    right: 22px;
    top: 26px;
    display: flex;
    flex-direction: column;
    gap: 14px;
  }
  .product-list--dense { gap: 8px; top: 18px; }
  .product {
    display: grid;
    grid-template-columns: 56px 1fr;
    gap: 12px;
    align-items: start;
  }
  .bottle {
    position: relative;
    width: 44px;
    height: 84px;
    margin: 4px auto 0;
  }
  .bottle-cap {
    position: absolute;
    left: 8px;
    top: 0;
    width: 28px;
    height: 12px;
    border-radius: 3px 3px 1px 1px;
    background: linear-gradient(90deg, var(--bottle-dark), var(--bottle-shine), var(--bottle-dark));
  }
  .bottle-body {
    position: absolute;
    left: 0;
    top: 13px;
    width: 44px;
    height: 71px;
    border-radius: 8px 8px 5px 5px;
    background: linear-gradient(90deg, var(--bottle-dark) 0%, var(--bottle) 45%, var(--bottle-shine) 60%, var(--bottle-dark) 100%);
    box-shadow: 0 4px 6px rgba(0,0,0,0.15);
  }
  .product-name {
    display: inline-block;
    background: var(--leaf);
    color: #fff;
    font-weight: 700;
    font-size: 9px;
    letter-spacing: 0.3px;
    padding: 3px 6px;
    margin-bottom: 4px;
    text-transform: uppercase;
  }
  .product-text {
    font-size: 7.2px;
    line-height: 1.38;
  }
  .product-text b { font-weight: 700; }
  .brand {
    position: absolute;
    text-align: right;
  }
  .brand-name {
    font-weight: 500;
    color: var(--leaf-dark);
    line-height: 1;
    display: flex;
    align-items: center;
    gap: 6px;
    justify-content: flex-end;
  }
  .brand-dot {
    display: inline-block;
    border-radius: 50%;
    background: var(--leaf-dark);
  }
  .brand-tagline {
    color: var(--bark-light);
    font-weight: 500;
    margin-top: 4px;
  }
  .brand--cover { top: 92px; right: 36px; }
  .brand--cover .brand-name { font-size: 44px; }
  .brand--cover .brand-dot { width: 10px; height: 10px; }
  .brand--cover .brand-tagline { font-size: 13px; }
  .brand--back { left: 122px; top: 478px; }
  .brand--back .brand-name { font-size: 22px; }
  .brand--back .brand-dot { width: 6px; height: 6px; }
  .brand--back .brand-tagline { font-size: 7px; }
  .cover-photo {
    position: absolute;
    left: 150px;
    top: 330px;
    width: 180px;
    height: 210px;
    border-radius: 24px;
    background: linear-gradient(160deg, #b6d96a 0%, #6fa83a 38%, #a62535 62%, #5e0e1a 100%);
  }
  .back-decor {
    position: absolute;
    left: 0;
    top: 400px;
    width: 160px;
    height: 160px;
    border-top-right-radius: 160px;
    background: linear-gradient(160deg, #6b3a1a 0%, #6b3a1a 30%, #a6cf3a 55%, #6fae2c 100%);
  }
</style>
</head>
<body>

<section class="spread spread--outer">
  <article class="page page--back">
    <div class="product-list">
      <div class="product">
        <div class="bottle" role="img" aria-label="Photo of a bitter melon supplement bottle"><span class="bottle-cap"></span><span class="bottle-body"></span></div>
        <div>
          <span class="product-name">Bitter Melon</span>
          <p class="product-text">Lorem Ipsum is simply dummy text of the printing and typesetting industry. Lorem Ipsum dummy text ever since the 1500s.<br>
          <b>Pack size:</b> 60 veg capsules<br>
          <b>Adult Dosage:</b> Lorem Ipsum is simply dummy text of the printing and typesetting industry.<br>
          <b>Storage:</b> Store in a cool, dry place after opening.<br>
          <b>Warnings:</b> For adults only. Consult physician if pregnant/lactating, taking medication or have a medical condition.</p>
        </div>
      </div>
      <div class="product">
        <div class="bottle" role="img" aria-label="Photo of a brain booster supplement bottle"><span class="bottle-cap"></span><span class="bottle-body"></span></div>
        <div>
          <span class="product-name">Brain Booster</span>
          <p class="product-text">Lorem Ipsum is simply dummy text of the printing and typesetting industry. Lorem Ipsum has been the industry's standard dummy text ever since the 1500s.<br>
          <b>Pack size:</b> 60 veg capsules<br>
          <b>Adult Dosage:</b> Lorem Ipsum is simply dummy text of the printing and typesetting industry.<br>
          <b>Storage:</b> Store in a cool, dry place after opening.<br>
          <b>Warnings:</b> For adults only. Consult physician if pregnant/lactating, taking medication or have a medical condition.</p>
        </div>
      </div>
    </div>
    <div class="back-decor" role="img" aria-label="Decorative brown and green leaf artwork"></div>
    <div class="brand brand--back">
      <div class="brand-name"><span class="brand-dot"></span>Verdalia</div>
      <div class="brand-tagline">Natural Nutrition</div>
    </div>
  </article>

  <article class="page page--cover">
    <svg class="page-art" viewBox="0 0 390 560" aria-hidden="true">
      <defs>
        <linearGradient id="coverGreen" x1="1" y1="0" x2="0" y2="1">
          <stop offset="0" stop-color="#a8d64a"/><stop offset="0.55" stop-color="#dff0b8"/><stop offset="1" stop-color="#ffffff"/>
        </linearGradient>
        <linearGradient id="coverBark" x1="0" y1="1" x2="1" y2="0">
          <stop offset="0" stop-color="#6b3a1a"/><stop offset="1" stop-color="#3d1d0b"/>
        </linearGradient>
      </defs>
      <path d="M100 0 L390 0 L390 560 L280 560 C330 420 140 240 130 120 C125 60 110 20 100 0 Z" fill="url(#coverGreen)"/>
      <path d="M0 560 C30 470 110 400 230 390 C300 385 360 400 390 420 L390 560 Z" fill="url(#coverBark)"/>
    </svg>
    <div class="cover-photo" role="img" aria-label="Leaf-shaped artwork framing photos of fresh tea leaves and ripe cranberries"></div>
    <div class="brand brand--cover">
      <div class="brand-name"><span class="brand-dot"></span>Verdalia</div>
      <div class="brand-tagline">Natural Nutrition</div>
    </div>
  </article>
</section>

<section class="spread spread--inner">
  <article class="page">
    <div class="product-list product-list--dense">
      <div class="product">
        <div class="bottle" role="img" aria-label="Photo of a green tea extract supplement bottle"><span class="bottle-cap"></span><span class="bottle-body"></span></div>
        <div>
          <span class="product-name">Green Tea Extract</span>
          <p class="product-text">Lorem Ipsum is simply dummy text of the printing and typesetting industry. Lorem Ipsum has been the industry's standard dummy text ever since the 1500s.<br>
          <b>Pack size:</b> 60 veg capsules<br>
          <b>Adult Dosage:</b> Lorem Ipsum is simply dummy text of the printing and typesetting industry.<br>
          <b>Storage:</b> Store in a cool, dry place after opening.<br>
          <b>Warnings:</b> For adults only. Consult physician if pregnant/lactating, taking medication or have a medical condition.</p>
        </div>
      </div>
      <div class="product">
        <div class="bottle" role="img" aria-label="Photo of a garcinia cambogia and turmeric supplement bottle"><span class="bottle-cap"></span><span class="bottle-body"></span></div>
        <div>
          <span class="product-name">Garcinia Cambogia+Turmeric</span>
          <p class="product-text">Lorem Ipsum is simply dummy text of the printing and typesetting industry. Lorem Ipsum has been the industry's standard dummy text ever since the 1500s.<br>
          <b>Pack size:</b> 60 veg capsules<br>
          <b>Adult Dosage:</b> Lorem Ipsum is simply dummy text of the printing and typesetting industry.<br>
          <b>Storage:</b> Store in a cool, dry place after opening.<br>
          <b>Warnings:</b> For adults only. Consult physician if pregnant/lactating, taking medication or have a medical condition.</p>
        </div>
      </div>
      <div class="product">
        <div class="bottle" role="img" aria-label="Photo of a turmeric energy supplement bottle"><span class="bottle-cap"></span><span class="bottle-body"></span></div>
        <div>
          <span class="product-name">Turmeric Energy</span>
          <p class="product-text">Lorem Ipsum is simply dummy text of the printing and typesetting industry. Lorem Ipsum has been the industry's standard dummy text ever since the 1500s.<br>
          <b>Pack size:</b> 60 veg capsules<br>
          <b>Adult Dosage:</b> Lorem Ipsum is simply dummy text of the printing and typesetting industry.<br>
          <b>Storage:</b> Store in a cool, dry place after opening.<br>
          <b>Warnings:</b> For adults only. Consult physician if pregnant/lactating, taking medication or have a medical condition.</p>
        </div>
      </div>
      <div class="product">
        <div class="bottle" role="img" aria-label="Photo of a cranberry supplement bottle"><span class="bottle-cap"></span><span class="bottle-body"></span></div>
        <div>
          <span class="product-name">Cranberry</span>
          <p class="product-text">Lorem Ipsum is simply dummy text of the printing and typesetting industry. Lorem Ipsum has been the industry's standard dummy text ever since the 1500s.<br>
          <b>Pack size:</b> 60 veg capsules<br>
          <b>Adult Dosage:</b> Lorem Ipsum is simply dummy text of the printing and typesetting industry.<br>
          <b>Storage:</b> Store in a cool, dry place after opening.<br>
          <b>Warnings:</b> For adults only. Consult physician if pregnant/lactating.</p>
        </div>
      </div>
    </div>
  </article>

  <article class="page page--tinted">
    <div class="product-list product-list--dense">
      <div class="product">
        <div class="bottle" role="img" aria-label="Photo of a bitter melon supplement bottle"><span class="bottle-cap"></span><span class="bottle-body"></span></div>
        <div>
          <span class="product-name">Bitter Melon</span>
          <p class="product-text">Lorem Ipsum is simply dummy text of the printing and typesetting industry. Lorem Ipsum dummy text ever since the 1500s.<br>
          <b>Pack size:</b> 60 veg capsules<br>
          <b>Adult Dosage:</b> Lorem Ipsum is simply dummy text of the printing and typesetting industry.<br>
          <b>Storage:</b> Store in a cool, dry place after opening.<br>
          <b>Warnings:</b> For adults only. Consult physician if pregnant/lactating, taking medication or have a medical condition.</p>
        </div>
      </div>
      <div class="product">
        <div class="bottle" role="img" aria-label="Photo of a brain booster supplement bottle"><span class="bottle-cap"></span><span class="bottle-body"></span></div>
        <div>
          <span class="product-name">Brain Booster</span>
          <p class="product-text">Lorem Ipsum is simply dummy text of the printing and typesetting industry. Lorem Ipsum has been the industry's standard dummy text ever since the 1500s.<br>
          <b>Pack size:</b> 60 veg capsules<br>
          <b>Adult Dosage:</b> Lorem Ipsum is simply dummy text of the printing and typesetting industry.<br>
          <b>Storage:</b> Store in a cool, dry place after opening.<br>
          <b>Warnings:</b> For adults only. Consult physician if pregnant/lactating, taking medication or have a medical condition.</p>
        </div>
      </div>
      <div class="product">
        <div class="bottle" role="img" aria-label="Photo of a noni resveratrol supplement bottle"><span class="bottle-cap"></span><span class="bottle-body"></span></div>
        <div>
          <span class="product-name">Noni Resveratrol</span>
          <p class="product-text">Lorem Ipsum is simply dummy text of the printing and typesetting industry. Lorem Ipsum has been the industry's standard dummy text ever since the 1500s.<br>
          <b>Pack size:</b> 60 veg capsules<br>
          <b>Adult Dosage:</b> Lorem Ipsum is simply dummy text of the printing and typesetting industry.<br>
          <b>Storage:</b> Store in a cool, dry place after opening.<br>
          <b>Warnings:</b> For adults only. Consult physician if pregnant/lactating, taking medication or have a medical condition.</p>
        </div>
      </div>
      <div class="product">
        <div class="bottle" role="img" aria-label="Photo of a longevity formula supplement bottle"><span class="bottle-cap"></span><span class="bottle-body"></span></div>
        <div>
          <span class="product-name">Longevity Formal</span>
          <p class="product-text">Lorem Ipsum is simply dummy text of the printing and typesetting industry. Lorem Ipsum has been the industry's standard dummy text ever since the 1500s.<br>
          <b>Pack size:</b> 60 veg capsules<br>
          <b>Adult Dosage:</b> Lorem Ipsum is simply dummy text of the printing and typesetting industry.<br>
          <b>Storage:</b> Store in a cool, dry place after opening.<br>
          <b>Warnings:</b> For adults only. Consult physician if pregnant/lactating.</p>
        </div>
      </div>
    </div>
  </article>
</section>

</body>
</html>
```